Book Cover Design | Science & Nature

We are looking for a cover design for our new educational book titled "Moths Beyond the Hedge".
The full title on the cover can either only be "Moths Beyond the Hedge" or "Garden Moths Beyond the Hedge - a pocket handbook". Up to you what looks good. If the latter, the words "Moths Beyond the Hedge" should be written in larger letters.
The book has a lot information about spiders in general and provides a convenient and understandable identification guide about spiders in California.
The target audience are normal, non-scientist readers who would like to get a simple guide that helps them identify common spiders they will find inside their homes and gardens.
The book is written in an understandable, non-scientific language and contains numerous illustrations and identification sheets of all common spiders.
We are fairly open to suggestions about the design. It should not be too plain as it is not a classic boring science book, but aimed at the average reader. Readers are both male and female, aged 30 and above.
If you know nothing about spiders but would like to know what the spiders in your backyard are, which ones are dangerous and if you want to learn more about spiders, this should be the book you will want to buy!
The author is Dale Prowse. In addition to the author, the book cover should show "Brindlewing.com" - The author can be at the bottom and the website on the top or vice versa.
The cover size is 6" x 9" (15.24 x 22.86 cm). The book has around 150 pages. The back of the book should have a placeholder for the barcode as well as some text. It should also have a quick overview of the main benefits of the book: Easily understandable for non-scientist readers, helpful illustrations, tips on how to deal with spiders in the house and with spider bites. We will obviously add the text later.
I've attached a few of the illustrations as I think they could be used to already give the reader a feeling what they will get with the book. If you think a stock photo will work better than the illustrations, that is fine too.

Target Market(s)

Average readers in the United States wanting to learn more about spiders

Industry/Entity Type

Science, Nature, Spiders, Animals, Education

Requirements
Must have
• When the artwork is generated, the files we would like to receive are: The original working file PSD (Photoshop Document - so any text and images can be edited) All the working elements including: illustrations, photos, graphics and fonts A high resolution (300 dpi), 8.5 x 11 (o- Once r larger) file A JPG file in the exact size specifications and color required by our publisher A JPG file in the exact size for online POD or ebook (Pagelume requires 900x600 ) A JPG black and white (gray scale) variation
Nice to have
• A text (overlay?) could point out some of the advantages of this book: Illustrations and identification guides for all common California spiders, tips on how to get rid of spiders from inside the house, tips on how to deal with arachnophobia, etc. This is optional. Maybe something like "An easy to understand identification guide with plenty of tips and illustrations".
Should not have
• Very dark colors or very feminine colors or shapes.

```html
<!DOCTYPE html>
<html lang="en">
<head>
<meta charset="utf-8">
<title>Garden Moths Beyond the Hedge – Cover Spread</title>
<link rel="stylesheet" href="https://fonts.googleapis.com/css2?family=Cinzel:wght@700;900&family=Roboto+Condensed:wght@500&family=Arimo:wght@400&display=swap">
<style>
  :root {
    --stage: #e8edf1;
    --cover: #666666;
    --white: #ffffff;
    --ink: #0d0d0d;
    --gold: #fdb913;
    --leaf-light: #8cc063;
    --leaf-mid: #4f8f3a;
    --leaf-dark: #2f6a2a;
    --web: #c9cccf;
    --street: #8a8f8c;
  }
  * { margin: 0; padding: 0; box-sizing: border-box; }
  html, body { width: 1200px; height: 859px; overflow: hidden; background: var(--stage); }
  .spread {
    position: absolute; left: 27px; top: 20px; width: 1146px; height: 819px;
    background: var(--cover); box-shadow: 0 4px 14px rgba(0,0,0,.25); overflow: hidden;
  }
  .display { font-family: "Cinzel", serif; font-weight: 700; line-height: 1; }
  .site { font-family: "Roboto Condensed", sans-serif; font-weight: 500; line-height: 1; }
  .body-copy { font-family: "Arimo", sans-serif; font-size: 12px; line-height: 14.8px; color: var(--white); }

  /* back cover */
  .back-author { position: absolute; left: 0; width: 550px; top: 82px; text-align: center; font-size: 29px; color: var(--ink); }
  .back-title { position: absolute; left: 0; width: 550px; top: 130px; text-align: center; font-size: 24px; color: var(--white); }
  .back-title .accent { color: var(--gold); }
  .back-subtitle { position: absolute; left: 0; width: 550px; top: 167px; text-align: center; font-size: 24px; letter-spacing: 1px; color: var(--white); }
  .back-intro { position: absolute; left: 63px; top: 257px; width: 430px; }
  .back-photo-slot { position: absolute; left: 63px; top: 362px; width: 115px; height: 178px; background: var(--white); }
  .back-benefits { position: absolute; left: 197px; top: 356px; width: 296px; }
  .back-site { position: absolute; left: 314px; width: 178px; top: 650px; text-align: center; font-size: 19px; letter-spacing: 1.6px; color: var(--ink); }
  .barcode-slot { position: absolute; left: 314px; top: 681px; width: 178px; height: 102px; background: var(--white); }

  /* spine */
  .spine-text { position: absolute; left: 561px; writing-mode: vertical-rl; color: var(--ink); font-size: 17px; white-space: nowrap; }
  .spine-author { top: 73px; }
  .spine-title { top: 262px; font-size: 14px; }

  /* front cover */
  .cover-art { position: absolute; left: 600px; top: 360px; width: 546px; height: 459px; }
  .front-site { position: absolute; left: 775px; width: 220px; top: 42px; text-align: center; font-size: 27px; color: var(--white); }
  .front-author { position: absolute; left: 745px; width: 280px; top: 80px; text-align: center; font-size: 36px; color: var(--ink); }
  .title-block { position: absolute; right: 32px; top: 138px; text-align: right; z-index: 1; }
  .title-block span { display: block; }
  .t-garden { font-size: 42px; color: var(--white); }
  .t-moths { font-size: 96px; line-height: .9; color: var(--gold); font-weight: 900; }
  .t-beyond { font-size: 34px; color: var(--gold); font-weight: 900; margin-top: -2px; }
  .t-hedge { font-size: 100px; line-height: .9; color: var(--white); font-weight: 900; }
  .t-handbook { font-size: 32px; color: var(--white); margin-top: 6px; font-family: "Roboto Condensed", sans-serif; font-weight: 500; letter-spacing: 2px; text-transform: uppercase; }
</style>
</head>
<body>
<main class="spread">
  <section class="back-cover">
    <div class="back-author display">Dale Prowse</div>
    <div class="back-title display">Garden <span class="accent">Moths Beyond the</span> Hedge</div>
    <div class="back-subtitle site">A POCKET HANDBOOK</div>
    <p class="back-intro body-copy">Lorem ipsum dolor sit amet, consectetur adipisci elit, sed eiusmod tempor incidunt ut labore et dolore magna aliqua. Ut enim ad minim veniam, quis nostrum exercitationem ullam corporis suscipit laboriosam, nisi ut aliquid ex ea commodi consequatur. Quis aute iure reprehenderit in voluptate velit esse cillum dolore eu fugiat nulla pariatur. Excepteur sint obcaecat cupiditat non proident, sunt in culpa qui officia deserunt mollit anim id est laborum.</p>
    <div class="back-photo-slot"></div>
    <p class="back-benefits body-copy">Lorem ipsum dolor sit amet, consectetur adipisci elit, sed eiusmod tempor incidunt ut labore et dolore magna aliqua. Ut enim ad minim veniam, quis nostrum exercitationem ullam corporis suscipit laboriosam, nisi ut aliquid ex ea commodi consequatur. Quis aute iure reprehenderit in voluptate velit esse cillum dolore eu fugiat nulla pariatur. Excepteur sint obcaecat cupiditat non proident, sunt in culpa qui officia deserunt mollit anim id est laborum.</p>
    <div class="back-site site">Brindlewing.com</div>
    <div class="barcode-slot"></div>
  </section>

  <section class="spine">
    <div class="spine-text spine-author display">Dale Prowse</div>
    <div class="spine-text spine-title display">Garden Moths Beyond the Hedge - a pocket handbook</div>
  </section>

  <section class="front-cover">
    <svg class="cover-art" viewBox="0 0 546 459" role="img" aria-label="Illustration of garden creatures on a web and leafy treetops above a suburban street, with a hand holding a magnifying glass over one of them">
      <defs>
        <linearGradient id="scene-tones" x1="0" y1="0" x2="0.35" y2="1">
          <stop offset="0" stop-color="var(--web)"/>
          <stop offset="0.25" stop-color="var(--leaf-light)"/>
          <stop offset="0.55" stop-color="var(--leaf-mid)"/>
          <stop offset="0.8" stop-color="var(--leaf-dark)"/>
          <stop offset="1" stop-color="var(--street)"/>
        </linearGradient>
        <radialGradient id="scene-fade" cx="0.58" cy="0.55" r="0.62">
          <stop offset="0.55" stop-color="#fff"/>
          <stop offset="1" stop-color="#000"/>
        </radialGradient>
        <mask id="scene-mask">
          <rect width="546" height="459" fill="url(#scene-fade)"/>
        </mask>
      </defs>
      <rect width="546" height="459" fill="url(#scene-tones)" mask="url(#scene-mask)"/>
    </svg>
    <div class="front-site site">Brindlewing.com</div>
    <div class="front-author display">Dale Prowse</div>
    <h1 class="title-block display">
      <span class="t-garden">Garden</span>
      <span class="t-moths">Moths</span>
      <span class="t-beyond">Beyond the</span>
      <span class="t-hedge">Hedge</span>
      <span class="t-handbook">A pocket handbook</span>
    </h1>
  </section>
</main>
</body>
</html>
```